" UNFADING SPRINGTIDE 2020 ".

I want a flyer to invite people to a 2 Days Miracle Service. Salvation, Deliverance, Healing, Restoration, Breakthrough .
The best flyer you can propose me. Insert the logo i send you on the flyer. 04/11-04/12/2020. From 6:00Pm-10:00Pm. Venue: 5:00Pm. With Evangelist PAUL-HENRI MADOLEBA. ( LAMP & RIVER Ministry ) At: Tenbury Fellowship Hall. 24730 PELDRA Street, Romulus, Michigan 48174. Jesus-Christ Is the Lord.
Contact: - email : lampriverfel@outlook-mail.example
- cell phone: 5550419826
- Whatsapp :5550419826

Target Market(s)

Michigan, all ages

Font styles to use
Decorative
Script

Requirements
Must have
• Must have the logo of the ministry.

```html
<!DOCTYPE html>
<html lang="en">
<head>
<meta charset="utf-8">
<title>Two Days Miracle Service – Unfading Springtide 2020</title>
<link rel="stylesheet" href="https://fonts.googleapis.com/css2?family=Oswald:wght@400;500;600&family=Oxanium:wght@700;800&family=Open+Sans:ital,wght@0,600;1,800&display=swap">
<style>
  :root {
    --sky-top: #3a4f8f;
    --sky-mid: #7a4f9a;
    --sky-pink: #c8587e;
    --sky-haze: #b9a6d6;
    --crowd: #1c2450;
    --band: #101a42;
    --navy-text: #15183a;
    --white: #ffffff;
    --lavender: #e4dcf2;
    --faint: rgba(255, 255, 255, 0.16);
    --gold-a: #f6d8c6;
    --gold-b: #d9805e;
    --gold-c: #fff1e4;
    --outline: #3b1e2a;
    --icon-yellow: #f4d21d;
    --icon-green: #2fbf4b;
  }
  * { margin: 0; padding: 0; box-sizing: border-box; }
  html, body { width: 933px; height: 1200px; overflow: hidden; background: var(--band); }
  .flyer {
    position: relative; width: 933px; height: 1200px; overflow: hidden;
    font-family: "Oswald", sans-serif; color: var(--white);
  }
  .backdrop {
    position: absolute; inset: 0;
    background:
      radial-gradient(ellipse 420px 300px at 640px 620px, rgba(225, 215, 245, 0.85), transparent 70%),
      radial-gradient(ellipse 500px 220px at 300px 470px, rgba(214, 90, 130, 0.75), transparent 70%),
      linear-gradient(180deg, var(--sky-top) 0%, #5b5aa0 22%, var(--sky-mid) 38%, var(--sky-pink) 50%, var(--sky-haze) 62%, #6c6aa6 76%, var(--crowd) 90%);
  }
  .evangelist-photo {
    position: absolute; left: 84px; top: 383px; width: 400px; height: 560px;
    border-radius: 46% 46% 8px 8px / 30% 30% 8px 8px;
    background: linear-gradient(180deg, rgba(40, 40, 70, 0.55) 0%, rgba(150, 40, 80, 0.6) 55%, rgba(30, 30, 60, 0.7) 100%);
  }
  .virtues {
    position: absolute; top: 80px;
    writing-mode: vertical-rl; transform: rotate(180deg);
    font-family: "Open Sans", sans-serif; font-weight: 600;
    font-size: 42px; letter-spacing: 2px; color: var(--faint);
    white-space: nowrap; height: 940px; text-align: right;
  }
  .virtues-one { left: 80px; word-spacing: 28px; }
  .virtues-two { left: 146px; height: 850px; word-spacing: 10px; }
  .motto {
    position: absolute; top: 80px; left: 0; width: 933px; text-align: center;
    font-size: 21px; letter-spacing: 1.5px;
  }
  .ministry-mark {
    position: absolute; left: 401px; top: 117px; width: 130px; height: 130px;
    border-radius: 50%; background: #1a1a1f;
    display: flex; align-items: center; justify-content: center; text-align: center;
    font-family: "Oswald", sans-serif; font-weight: 500; font-size: 15px; line-height: 1.15;
    color: var(--white); padding: 14px;
  }
  .headline-kicker {
    position: absolute; left: 501px; top: 302px;
    font-family: "Open Sans", sans-serif; font-style: italic; font-weight: 800;
    font-size: 27px; letter-spacing: 2px; color: var(--lavender);
  }
  .headline {
    position: absolute; left: 485px; font-family: "Oxanium", sans-serif; font-weight: 800;
    font-size: 82px; line-height: 1; letter-spacing: 1px;
    background: linear-gradient(170deg, var(--gold-c) 0%, var(--gold-a) 30%, var(--gold-b) 55%, var(--gold-c) 80%, var(--gold-b) 100%);
    -webkit-background-clip: text; background-clip: text; color: transparent;
    -webkit-text-stroke: 2px var(--outline);
  }
  .headline-miracle { top: 342px; }
  .headline-service { top: 432px; }
  .speaker { position: absolute; left: 487px; top: 520px; color: var(--navy-text); }
  .speaker-intro { font-size: 26px; font-weight: 500; line-height: 1.2; }
  .speaker-name { font-size: 37px; font-weight: 600; letter-spacing: 1px; line-height: 1.25; }
  .speaker-ministry { font-size: 26px; font-weight: 500; line-height: 1.3; }
  .details {
    position: absolute; left: 0; width: 933px; text-align: center;
    font-weight: 500; line-height: 1; text-shadow: 0 2px 6px rgba(0, 0, 0, 0.45);
  }
  .details-dates { top: 886px; font-size: 31px; }
  .details-dates sup { font-size: 15px; vertical-align: 14px; }
  .details-time { top: 936px; font-size: 30px; }
  .details-venue { top: 987px; font-size: 30px; }
  .details-address { top: 1022px; font-size: 30px; }
  .contact-band {
    position: absolute; left: 0; top: 1054px; width: 933px; height: 146px;
    background: linear-gradient(180deg, rgba(16, 26, 66, 0.6), var(--band) 40%);
  }
  .contact-email {
    position: absolute; left: 62px; top: 1093px; display: flex; align-items: center; gap: 14px;
    font-family: "Open Sans", sans-serif; font-weight: 600; font-size: 20px;
  }
  .contact-phone {
    position: absolute; left: 512px; top: 1086px; display: flex; align-items: center; gap: 10px;
    font-family: "Open Sans", sans-serif; font-weight: 600; font-size: 32px;
  }
  .chat-dot { width: 34px; height: 34px; border-radius: 50%; background: var(--icon-green); }
  .phone-number { margin-left: 8px; }
</style>
</head>
<body>
<main class="flyer">
  <div class="backdrop" role="img" aria-label="Evening sky in blue, violet and pink over a worshipping crowd with raised hands"></div>

  <div class="virtues virtues-one" aria-hidden="true">SALVATION DELIVERANCE HEALING</div>
  <div class="virtues virtues-two" aria-hidden="true">RESTORATION BREAKTHROUGH</div>

  <div class="evangelist-photo" role="img" aria-label="Evangelist in a dark jacket and red shirt singing into a microphone with one hand raised"></div>

  <p class="motto">JESUS CHRIST IS THE LORD.</p>
  <div class="ministry-mark">LAMP &amp; RIVER Ministries</div>

  <p class="headline-kicker">TWO DAYS</p>
  <h1>
    <span class="headline headline-miracle">MIRACLE</span>
    <span class="headline headline-service">SERVICE</span>
  </h1>

  <div class="speaker">
    <p class="speaker-intro">With Evangelist</p>
    <p class="speaker-name">PAUL-HENRI MADOLEBA</p>
    <p class="speaker-ministry">( LAMP &amp; RIVER Ministry )</p>
  </div>

  <p class="details details-dates">SATURDAY, APRIL 11<sup>TH</sup> &amp; SUNDAY, APRIL 12<sup>TH</sup>, 2020</p>
  <p class="details details-time">6.00 PM TO 10.00 PM</p>
  <p class="details details-venue">@ ST. TENBURY FELLOWSHIP HALL</p>
  <p class="details details-address">24730 PELDRA STREET, ROMULUS, MICHIGAN 48174</p>

  <div class="contact-band"></div>
  <div class="contact-email">
    <svg width="30" height="22" viewBox="0 0 30 22" aria-hidden="true">
      <rect x="1" y="1" width="28" height="20" fill="none" stroke="var(--icon-yellow)" stroke-width="2"/>
      <path d="M1 1 L15 12 L29 1 M1 21 L11 10 M29 21 L19 10" fill="none" stroke="var(--icon-yellow)" stroke-width="2"/>
    </svg>
    <span>lampriverfel@outlook-mail.example</span>
  </div>
  <div class="contact-phone">
    <svg width="36" height="36" viewBox="0 0 36 36" aria-hidden="true">
      <circle cx="18" cy="18" r="16" fill="none" stroke="var(--icon-yellow)" stroke-width="2.5"/>
      <path d="M13 9 L16 13 L14 15 Q16 20 21 22 L23 20 L27 23 L25 26 Q15 26 10 12 Z" fill="var(--icon-yellow)"/>
    </svg>
    <span class="chat-dot" aria-hidden="true"></span>
    <span class="phone-number">55504 19826</span>
  </div>
</main>
</body>
</html>
```